RLW CONSTRUCTION CO POSTCARD DESIGN

I was thinking of making a postcard for mailings by printmoor and or by me dropping off at homes . I guess it would be used as a mailing post card and or flyer . I have had sketch harbor design my buisnes cards . The buisness card design is a different version from my signage on trucks because of space . I have a logo design . thyat i can upload . I like silver for back ground and black for logo and letters with glossy finish . I would like to have the RLW with a back drop to give it depth , it would be the same color as windows .

The file i submitted ha a design with red letters , this design is more detailed than the other and should be used . The colors should be black on a silver card glossy . The windows and maybe give the letters depth with a backdrop outline . I want to let home owners know that they can always call for consultation and and repairs or maintenance for their home .

Target Market(s)

home owners

Industry/Entity Type

Construction

Other font styles liked:
• The same font as used in the picture of the sign i uploaded

Requirements
Must have
• HOME IMPROVEMENTS , MAINTENANCE AND REPAIRS , CARPENTRY , TILE PAINTING ECT

```html
<!DOCTYPE html>
<html lang="en">
<head>
<meta charset="utf-8">
<title>RLW Construction Co. Postcard</title>
<link href="https://fonts.googleapis.com/css2?family=EB+Garamond:wght@400;500&family=Lato:wght@400&display=swap" rel="stylesheet">
<style>
  :root {
    --ink: #000000;
    --paper: #ffffff;
    --silver: #a8a6a7;
    --stage: #8c8c8c;
    --guide: #c4c4c4;
    --serif: "EB Garamond", Garamond, Georgia, serif;
    --sans: "Lato", Arial, sans-serif;
  }
  * { box-sizing: border-box; margin: 0; padding: 0; }
  html, body { width: 1200px; height: 649px; overflow: hidden; }
  body { background: var(--stage); position: relative; font-family: var(--serif); color: var(--ink); }

  .card { position: absolute; top: 39px; width: 547px; height: 433px; background: var(--paper); overflow: hidden; }
  .card--front { left: 50px; }
  .card--back { left: 619px; }

  /* Front */
  .headline-band { position: absolute; left: 0; top: 0; width: 100%; height: 165px; background: var(--ink); color: var(--paper);
    display: flex; align-items: center; justify-content: center; text-align: center; }
  .headline-band h1 { font-weight: 500; font-size: 50px; line-height: 41px; letter-spacing: 0.2px; padding-top: 4px; }

  .brand { position: absolute; display: flex; flex-direction: column; align-items: flex-start; }
  .brand__name { font-weight: 500; color: var(--ink); line-height: 1.05; white-space: nowrap; }
  .card--front .brand { left: 26px; top: 258px; width: 210px; }
  .card--front .brand__name { font-size: 28px; }

  .contact { position: absolute; font-weight: 400; white-space: nowrap; }
  .contact__web, .contact__phone, .contact__address { display: block; }
  .card--front .contact { left: 252px; top: 225px; width: 288px; text-align: center; }
  .card--front .contact__web { font-size: 29px; line-height: 34px; }
  .card--front .contact__phone { font-size: 45px; line-height: 48px; }
  .card--front .contact__address { font-size: 19px; line-height: 22px; }

  .services-band { position: absolute; left: 0; bottom: 0; width: 100%; height: 55px; background: var(--ink); color: var(--paper);
    display: flex; align-items: center; justify-content: center; font-size: 12.5px; letter-spacing: 0.1px; white-space: nowrap; }

  /* Back */
  .card--back .brand { left: 20px; top: 56px; width: 145px; }
  .card--back .brand__name { font-size: 17px; }
  .card--back .contact { left: 174px; top: 34px; text-align: left; }
  .card--back .contact__web { font-size: 19px; line-height: 24px; padding-left: 1px; }
  .card--back .contact__phone { font-size: 29px; line-height: 30px; padding-left: 12px; }
  .card--back .contact__address { font-size: 13px; line-height: 15px; }
  .back-headline { position: absolute; left: 19px; top: 140px; font-weight: 500; font-size: 34px; line-height: 30px; }

  .postage-zone { position: absolute; left: 457px; top: 18px; width: 70px; height: 77px; border: 1.5px solid var(--guide);
    display: flex; align-items: center; justify-content: center; text-align: center; font-family: var(--sans); font-size: 14px; line-height: 18px; color: var(--guide); }
  .zone-label { position: absolute; font-family: var(--sans); color: var(--guide); white-space: nowrap; }
  .zone-label--mailing { left: 331px; top: 250px; font-size: 14px; }
  .zone-label--no-address { left: 75px; top: 322px; font-size: 12px; }
  .zone-label--barcode { left: 230px; top: 404px; font-size: 14px; }
</style>
</head>
<body>
  <section class="card card--front" aria-label="Postcard front">
    <div class="headline-band">
      <h1>Call for consultation,<br>repairs or<br>maintenance services.</h1>
    </div>
    <div class="brand">
      <span class="brand__name">RLW<br>Construction Co.</span>
    </div>
    <div class="contact">
      <span class="contact__web">rlwconstruction.com</span>
      <span class="contact__phone">617 555 0148</span>
      <span class="contact__address">27 Alder Row Boaton MA. 02130</span>
    </div>
    <div class="services-band">HOME IMPROVEMENTS , MAINTENANCE &amp; REPAIRS , CARPENTRY , TILE PAINTING ECT</div>
  </section>

  <section class="card card--back" aria-label="Postcard back">
    <div class="brand">
      <span class="brand__name">RLW<br>Construction Co.</span>
    </div>
    <div class="contact">
      <span class="contact__web">rlwconstruction.com</span>
      <span class="contact__phone">617 555 0148</span>
      <span class="contact__address">27 Alder Row Boaton MA. 02130</span>
    </div>
    <div class="postage-zone">Postage<br>Clear<br>Zone</div>
    <p class="back-headline">Call for<br>consultation,<br>repairs or<br>maintenance<br>services.</p>
    <span class="zone-label zone-label--mailing">Mailing address Area</span>
    <span class="zone-label zone-label--no-address">No Address in this area</span>
    <span class="zone-label zone-label--barcode">Barcode Area</span>
  </section>
</body>
</html>
```